Financial Book Cover Design (Subject: exponential technologies)

We are in need of a FRONT, BACK and SPINE design for an upcoming book titled: Quiet Harbor Plans: An Almanac For Every Season, Tide and Distant Shore.

REQUIREMENTS:
TITLE:Quiet Harbor Plans: An Almanac For Every Season, Tide and Distant Shore

PHOTOS: as designer sees fit, author must be on someplace.

SIZE OF BOOK:
Cove - 7.25 inches wide, 9.25 inches tall
Spine - 1.25 inches

ABOUT THE BOOK:
Advances in exponential technologies will affect virtually every aspect of life on our planet. Innovation will touch everything we do, from how we communicate to the way we manage our personal finances. They will affect how you’ll learn, work, live and love.

Advances in networks and computer systems, robotics, big data, nanotechnology, medicine and neuroscience, biotechnology, energy and environmental systems, materials science, and financial services technology are quickly changing everything. Due to such innovations as tennis rackets that track the speed of your forehand, backhand, serve or smash ($200, available now) to the world’s largest indoor, vertical farm that produces two million pounds of produce annually without soil or sunlight (Newark, New Jersey), your life will never be the same.

These shocking innovations will alter every aspect of your personal finances, from how long you’ll live (most likely, well into your 100s), when you’ll retire (you won’t, at least not for many decades), to where you work (not where you work now), what you do (you’ll engage in a new occupation, maybe several), how to save for college (you won’t have to) and pay for long-term care (ditto), choosing where to live (in communities built just for you), how you’ll save (adapting investment strategies that have never before existed) and how many spouses you’ll have and where you’ll find them (!).

Because of all the changes that are coming, it’s vital that you alter your strategies for handling your personal finances. If you manage your money the way prior generations managed theirs, you will fail where they succeeded.

• REQUIREMENTS:
• TITLE:Quiet Harbor Plans: An Almanac For Every Season, Tide and Distant Shore
• PHOTOS: as designer sees fit, author must be on someplace.
• SIZE OF BOOK:
• Cove - 7.25 inches wide, 9.25 inches tall
• Spine - 1.25 inches

```html
<!DOCTYPE html>
<html lang="en">
<head>
<meta charset="utf-8">
<title>Quiet Harbor Plans — Book Cover</title>
<link href="https://fonts.googleapis.com/css2?family=Cinzel:wght@500;700&family=Oswald:wght@500&family=Quicksand:wght@500&display=swap" rel="stylesheet">
<style>
  :root {
    --paper: #ffffff;
    --backdrop: #e7e6e2;
    --gold: #c9a645;
    --gold-deep: #b38f2e;
    --ink: #1c1c1c;
    --body-ink: #2b2b2b;
    --photo-light: #dcdcdc;
    --photo-dark: #2a2a2e;
  }
  * { margin: 0; padding: 0; box-sizing: border-box; }
  html, body {
    width: 1200px; height: 801px; overflow: hidden;
    background: var(--backdrop);
  }
  .book-wrap {
    position: absolute; left: 38px; top: 70px;
    width: 1124px; height: 660px;
    display: flex;
    box-shadow: 0 10px 30px rgba(0,0,0,.15);
  }
  /* ---------- Back cover ---------- */
  .back-cover {
    position: relative; width: 517px; height: 660px;
    background: var(--paper);
  }
  .back-frame {
    position: absolute; inset: 26px 24px 30px 24px;
    border: 1.5px solid var(--gold);
  }
  .back-author-photo {
    position: absolute; left: 46px; top: 44px;
    width: 80px; height: 84px;
    background: linear-gradient(180deg, var(--photo-light) 0%, #bfbfbf 45%, var(--photo-dark) 75%);
  }
  .back-blurb {
    position: absolute; left: 66px; top: 150px; width: 410px;
    font-family: "Quicksand", sans-serif; font-weight: 500;
    font-size: 10.6px; line-height: 1.42; color: var(--body-ink);
  }
  .back-blurb p { margin-bottom: 12px; }
  .back-blurb p + p { padding-left: 0; }
  .back-blurb .dropcap {
    font-size: 19px; line-height: 1; float: left; margin-right: 2px;
  }
  /* ---------- Spine ---------- */
  .spine {
    position: relative; width: 90px; height: 660px;
    background: var(--paper);
    border-left: 1px solid #ececec; border-right: 1px solid #ececec;
  }
  .spine-title, .spine-subtitle {
    position: absolute; top: 38px;
    writing-mode: vertical-rl; white-space: nowrap;
  }
  .spine-title {
    left: 40px;
    font-family: "Cinzel", serif; font-weight: 700;
    font-size: 22px; letter-spacing: 1px; color: var(--gold);
  }
  .spine-subtitle {
    left: 14px;
    font-family: "Oswald", sans-serif; font-weight: 500;
    font-size: 15px; letter-spacing: .5px; color: var(--ink);
  }
  .spine-author {
    position: absolute; bottom: 26px; left: 0; width: 100%;
    text-align: center;
    font-family: "Cinzel", serif; font-weight: 700;
    font-size: 11px; color: var(--ink);
  }
  /* ---------- Front cover ---------- */
  .front-cover {
    position: relative; width: 517px; height: 660px;
    background: var(--paper); overflow: hidden;
  }
  .band-top {
    position: absolute; left: 0; top: 0; width: 100%; height: 32px;
    background: linear-gradient(180deg, var(--gold) 0%, var(--gold-deep) 100%);
  }
  .band-bottom {
    position: absolute; left: 0; bottom: 0; width: 100%; height: 58px;
    background: linear-gradient(180deg, var(--gold) 0%, var(--gold-deep) 100%);
  }
  .front-author-name {
    position: absolute; right: 34px; bottom: 16px;
    font-family: "Cinzel", serif; font-weight: 700;
    font-size: 20px; letter-spacing: 1px; color: var(--ink);
  }
  .front-author-photo {
    position: absolute; right: 34px; top: 100px;
    width: 230px; height: 502px;
    background: linear-gradient(180deg, var(--paper) 0%, #d9d6d0 18%, #3a3a3f 40%, var(--photo-dark) 100%);
    border-radius: 90px 90px 0 0;
  }
  .title-block {
    position: absolute; left: 40px; top: 66px;
    font-family: "Cinzel", serif; font-weight: 500;
    line-height: .98;
  }
  .title-line { display: block; }
  .title-line.gold { color: var(--gold); }
  .title-line.dark { color: var(--ink); font-weight: 700; }
  .title-line.l1 { font-size: 108px; }
  .title-line.l2 { font-size: 52px; letter-spacing: 1px; }
  .title-line.l3 { font-size: 62px; }
  .front-subtitle {
    position: absolute; left: 40px; top: 380px; width: 230px;
    font-family: "Oswald", sans-serif; font-weight: 500;
    font-size: 20px; line-height: 1.3; color: var(--gold-deep);
  }
</style>
</head>
<body>
  <main class="book-wrap">
    <section class="back-cover">
      <div class="back-frame"></div>
      <div class="back-author-photo" role="img" aria-label="Portrait photo of the author in a dark suit"></div>
      <div class="back-blurb">
        <p><span class="dropcap">A</span>dvances in exponential technologies will affect virtually every aspect of life on our planet. Innovation will touch everything we do, from how we communicate to the way we manage our personal finances. They will affect how you'll learn, work, live and love.</p>
        <p>Advances in networks and computer systems, robotics, big data, nanotechnology, medicine and neuroscience, biotechnology, energy and environmental systems, materials science, and financial services technology are quickly changing everything. Due to such innovations as tennis rackets that track the speed of your forehand, backhand, serve or smash ($200, available now) to the world's largest indoor, vertical farm that produces two million pounds of produce annually without soil or sunlight (Newark, New Jersey), your life will never be the same.</p>
        <p>These shocking innovations will alter every aspect of your personal finances, from how long you'll live (most likely, well into your 100s), when you'll retire (you won't, at least not for many decades), to where you work (not where you work now), what you do (you'll engage in a new occupation, maybe several), how to save for college (you won't have to) and pay for long-term care (ditto), choosing where to live (in communities built just for you), how you'll save (adapting investment strategies that have never before existed) and how many spouses you'll have and where you'll find them (!).</p>
      </div>
    </section>

    <section class="spine">
      <span class="spine-title">QUIET HARBOR PLANS</span>
      <span class="spine-subtitle">AN ALMANAC FOR EVERY SEASON, TIDE AND DISTANT SHORE</span>
      <span class="spine-author">HALVORSEN</span>
    </section>

    <section class="front-cover">
      <div class="band-top"></div>
      <div class="front-author-photo" role="img" aria-label="Photo of the author standing in a dark suit with open arms"></div>
      <h1 class="title-block">
        <span class="title-line gold l1">QUIET</span>
        <span class="title-line dark l2">HARBOR</span>
        <span class="title-line gold l3">PLANS</span>
      </h1>
      <p class="front-subtitle">AN ALMANAC FOR EVERY SEASON, TIDE AND DISTANT SHORE</p>
      <div class="band-bottom"></div>
      <span class="front-author-name">DORIAN HALVORSEN</span>
    </section>
  </main>
</body>
</html>
```